Corporate Brightfen business cards to be handed to investor, bankers etc. Needs to have a young feel

I need business cards designed for a technology company that provides uber-like rapid response on the security industry. I would like it simple but very cool and tasteful. See attached documents for artwork and colours to be used. Cut sheet describes business model. Card stock should be thicker than normal. I would like the one side to be just the art and the other to have the contact info with maybe the pin somewhere.

Target Market(s)

Investors

Industry/Entity Type

Business

Contact Information for Business Card

Would like the logo attached on one side with name address and other info on the other side.

Font styles to use
Other font styles liked:
• See existing logo

Colors
6b449b
886aae
e4daeb
ffffff

Requirements
Must have
• Name: Dorian Felkatsis
• Address: 47 Larkfield Avenue, Toronto, On, M6K2B7
• Tel: 416-7291846
• Email: rolo@brightfen.io
Nice to have
• See logo colours

```html
<!DOCTYPE html>
<html lang="en">
<head>
<meta charset="utf-8">
<title>Brightfen business card</title>
<link href="https://fonts.googleapis.com/css2?family=Jost:wght@400;500;700&display=swap" rel="stylesheet">
<style>
  :root {
    --purple-deep: #6b449b;
    --purple-mid: #886aae;
    --lilac: #e4daeb;
    --white: #ffffff;
    --paper: #ecebe7;
    --ink: #1c1c1c;
    --backdrop: #d9d6d2;
  }
  * { margin: 0; padding: 0; box-sizing: border-box; }
  html, body { width: 1200px; height: 918px; overflow: hidden; }
  body {
    background: var(--backdrop);
    font-family: "Jost", sans-serif;
    display: flex;
    flex-direction: column;
    align-items: center;
    justify-content: center;
    gap: 60px;
  }
  .card {
    position: relative;
    width: 600px;
    height: 343px;
    background: var(--paper);
    border-bottom: 6px solid var(--purple-mid);
    box-shadow: 0 6px 18px rgba(0,0,0,0.12);
  }

  /* Art side */
  .art-side .wordmark {
    position: absolute;
    left: 50%;
    top: 50%;
    transform: translate(-50%, -50%);
    display: flex;
    align-items: center;
    gap: 14px;
  }
  .art-side .wordmark-dot {
    width: 30px; height: 30px;
    border-radius: 50%;
    background: var(--purple-deep);
  }
  .art-side .wordmark-name {
    font-size: 58px;
    font-weight: 400;
    color: var(--purple-deep);
    letter-spacing: -0.5px;
  }
  .art-side .vertical-url {
    position: absolute;
    left: 46px;
    top: 50%;
    transform: translate(-50%, -50%) rotate(90deg);
    font-size: 14px;
    letter-spacing: 5px;
    color: #333;
    white-space: nowrap;
  }

  /* Contact side */
  .contact-side .brand {
    position: absolute;
    right: 40px;
    top: 50px;
    display: flex;
    align-items: center;
    gap: 10px;
  }
  .contact-side .brand-dot {
    width: 18px; height: 18px;
    border-radius: 50%;
    background: var(--purple-mid);
  }
  .contact-side .brand-name {
    font-size: 54px;
    font-weight: 400;
    color: var(--ink);
    line-height: 1;
    letter-spacing: -0.5px;
  }
  .contact-side .person-name {
    position: absolute;
    right: 40px;
    top: 122px;
    font-size: 18px;
    font-weight: 700;
    color: var(--purple-deep);
    letter-spacing: 0.3px;
    text-transform: uppercase;
  }
  .contact-side .details {
    position: absolute;
    left: 40px;
    bottom: 36px;
    font-size: 15px;
    line-height: 1.35;
    color: var(--ink);
  }
  .contact-side .address { margin-bottom: 4px; }
  .contact-side .line {
    display: flex;
    align-items: center;
    gap: 8px;
  }
  .contact-side .icon {
    width: 11px; height: 11px;
    fill: var(--purple-deep);
    flex: none;
  }
</style>
</head>
<body>

  <section class="card art-side">
    <span class="vertical-url">www.brightfen.io</span>
    <div class="wordmark">
      <span class="wordmark-dot"></span>
      <span class="wordmark-name">brightfen</span>
    </div>
  </section>

  <section class="card contact-side">
    <div class="brand">
      <span class="brand-dot"></span>
      <span class="brand-name">brightfen</span>
    </div>
    <div class="person-name">Dorian Felkatsis</div>

    <div class="details">
      <div class="address">47 Larkfield Avenue<br>Toronto, On, M6K2B7</div>
      <div class="line">
        <svg class="icon" viewBox="0 0 12 12" aria-hidden="true"><path d="M1 3.5C1 2 2 1 3 1h6c1 0 2 1 2 2.5v.8H8.5v-1h-5v1H1z"/><path d="M2.5 5h7l1 5.5H1.5z"/></svg>
        <span>416-7291846</span>
      </div>
      <div class="line">
        <svg class="icon" viewBox="0 0 12 12" aria-hidden="true"><path d="M0.5 2.5h11v1L6 7 0.5 3.5z"/><path d="M0.5 5l5.5 3.5L11.5 5v4.5h-11z"/></svg>
        <span>rolo@brightfen.io</span>
      </div>
      <div class="line">
        <svg class="icon" viewBox="0 0 12 12" aria-hidden="true"><circle cx="6" cy="6" r="5.5"/><path d="M6 1v10M1 6h10" stroke="#ecebe7" stroke-width="0.8"/></svg>
        <span>www.brightfen.io</span>
      </div>
    </div>
  </section>

</body>
</html>
```